Dalton Power Supply, Inc. Business Card Design

We are an Electrical Distributor looking for a Modern, Professional Business Card design.

Target Market(s)

Residential Commercial Industrial

Industry/Entity Type

Electrical

Contact Information for Business Card

Dalton Power Supply, Inc.
418 Maple Ridge Lane
Brookvale, NC 27514
555-214-7630
555-214-8842 Fax
daltonpower@brightmail-example.net

```html
<!DOCTYPE html>
<html lang="en">
<head>
<meta charset="utf-8">
<title>Dalton Power Supply, Inc. — Business Card</title>
<link rel="stylesheet" href="https://fonts.googleapis.com/css2?family=Arimo:wght@400&display=swap">
<style>
  :root {
    --card-white: #ffffff;
    --brand-yellow: #fdc300;
    --slate: #434e54;
    --page: #ffffff;
  }
  html, body {
    margin: 0;
    padding: 0;
    width: 1200px;
    height: 686px;
    overflow: hidden;
    background: var(--page);
  }
  .card {
    position: relative;
    width: 1200px;
    height: 686px;
    background: var(--card-white);
    font-family: "Arimo", Arial, sans-serif;
    font-weight: 400;
    overflow: hidden;
  }
  .card__swoosh {
    position: absolute;
    inset: 0;
    width: 1200px;
    height: 686px;
  }
  .address {
    position: absolute;
    margin: 0;
    color: var(--slate);
    font-size: 34px;
    letter-spacing: 1px;
    line-height: 1;
    font-style: normal;
  }
  .address__line { position: absolute; white-space: nowrap; }
  .address__company { left: 74px; top: 37px; }
  .address__street  { left: 98px; top: 83px; }
  .address__city    { left: 137px; top: 128px; }

  .contact {
    position: absolute;
    left: 31px;
    top: 520px;
    margin: 0;
    padding: 0;
    list-style: none;
    color: var(--card-white);
    letter-spacing: 1px;
  }
  .contact__item { white-space: nowrap; line-height: 1; }
  .contact__phone { font-size: 34px; }
  .contact__fax { font-size: 34px; margin-top: 13px; }
  .contact__email { font-size: 34px; margin-top: 22px; }

  .brand {
    position: absolute;
    left: 690px;
    top: 60px;
    width: 460px;
    display: flex;
    flex-direction: column;
    align-items: center;
    color: var(--brand-yellow);
  }
  .brand__mark {
    width: 150px;
    height: 150px;
    background: var(--brand-yellow);
    margin-bottom: 40px;
  }
  .brand__name {
    font-size: 74px;
    line-height: 1;
    white-space: nowrap;
  }
  .brand__tag {
    font-size: 34px;
    line-height: 1;
    margin-top: 14px;
    white-space: nowrap;
  }
</style>
</head>
<body>
  <main class="card">
    <svg class="card__swoosh" viewBox="0 0 1200 686" aria-hidden="true">
      <path d="M34,0 C250,420 600,640 1016,686 L0,686 L0,0 Z" fill="var(--brand-yellow)"/>
    </svg>

    <address class="address">
      <span class="address__line address__company">Dalton Power Supply, Inc.</span>
      <span class="address__line address__street">418 Maple Ridge Lane</span>
      <span class="address__line address__city">Brookvale, NC 27514</span>
    </address>

    <div class="brand">
      <div class="brand__mark" aria-hidden="true"></div>
      <div class="brand__name">Dalton Power</div>
      <div class="brand__tag">Supply, Inc.</div>
    </div>

    <ul class="contact">
      <li class="contact__item contact__phone">Phone: 555-214-7630</li>
      <li class="contact__item contact__fax">Fax: 555-214-8842</li>
      <li class="contact__item contact__email">daltonpower@brightmail-example.net</li>
    </ul>
  </main>
</body>
</html>
```